School and office cleaning at its best

We need a flyer for our mailing purposes to obtain new customers. Our name of the company is The Brightwells We have been in business since 2008 and are servicing multiple locations in san Jose CA our primary colors are black and white and red
We are servicing schools, offices, office buildings, gyms, dance studios,
We provide janitorial services weekly,biweekly and daily.
We have uniformed custodians.
We also provide carpet cleaning
Floors strip and wax
Floor steaming
Personal supervision
Quality control

Target Market(s)

Offices, schools, gyms, office buildings

Industry/Entity Type

Janitorial Service

Font styles to use
Serif

Colors

Designer to choose colors to be used in the design.

Requirements
Must have
• services provided
• Cleaning
• Carpet cleaning
• Floor strip and wax
• Floor steaming
• Janitorial services
• \Uniformed custodians
Nice to have
• surprise me
• Colors of black
• red
• white
• among others
Should not have
• Prices
• discounts

```html
<!DOCTYPE html>
<html lang="en">
<head>
<meta charset="utf-8">
<title>The Brightwells – Cleaning Flyer</title>
<link rel="stylesheet" href="https://fonts.googleapis.com/css2?family=Oswald:wght@300;400;700&family=Montserrat:wght@400;500;700;800&family=Dancing+Script:wght@700&display=swap">
<style>
:root{
  --ink:#121212;
  --ink-2:#1c1c1e;
  --band:#1a1a1a;
  --red:#c0131b;
  --red-deep:#8e0a10;
  --white:#ffffff;
  --silver:#cfcfcf;
  --grey:#8a8a8a;
}
*{margin:0;padding:0;box-sizing:border-box}
html,body{width:903px;height:1200px;overflow:hidden;background:#e9e9e9}
.flyer{
  position:relative;width:903px;height:1200px;overflow:hidden;
  background:radial-gradient(ellipse at 50% 30%,#2a2a2c 0%,var(--ink-2) 45%,var(--ink) 100%);
  font-family:'Montserrat',sans-serif;color:var(--white);
}
.abs{position:absolute}
.hand-art{left:443px;top:0;width:150px;height:130px}
.brand{left:150px;top:165px;width:603px;text-align:center}
.brand-name{font-family:'Montserrat',sans-serif;font-weight:800;font-size:56px;letter-spacing:.5px;color:var(--white);line-height:1}
.figure-art{left:168px;top:300px;width:140px;height:255px}
.headline-script{left:353px;top:268px;font-family:'Dancing Script',cursive;font-weight:700;font-size:62px;color:var(--red);line-height:1}
.headline-best{
  left:318px;top:318px;font-family:'Oswald',sans-serif;font-weight:700;font-size:258px;line-height:1;letter-spacing:-2px;
  background:linear-gradient(180deg,#ffffff 0%,#f2f2f2 45%,#bdbdbd 52%,#e8e8e8 100%);
  -webkit-background-clip:text;background-clip:text;color:transparent;
}
.intro{left:144px;top:588px;width:620px;text-align:center;font-size:13.2px;line-height:19px;color:var(--white)}
.services-lead{left:95px;top:680px;font-size:19px;font-weight:400}
.service-list{left:57px;top:710px;list-style:none}
.service-list li{display:flex;align-items:center;height:32px;font-weight:700;font-size:20px;color:var(--red)}
.service-list svg{width:24px;height:22px;margin-right:14px;fill:var(--grey)}
.rule-short{left:95px;top:878px;width:135px;height:1px;background:var(--red)}
.schedule{left:57px;top:893px;display:flex}
.schedule svg{width:24px;height:24px;margin-right:14px;margin-top:2px}
.schedule p{font-size:19px;line-height:30px}
.schedule strong{display:block;color:var(--red);font-weight:700;font-size:20px}
.rule-vertical{left:467px;top:742px;width:1px;height:182px;background:var(--red)}
.extras-pill{left:512px;top:682px;width:234px;height:36px;border-radius:18px;background:var(--red);font-weight:700;font-size:19px;display:flex;align-items:center;justify-content:center}
.extras-line{left:740px;top:698px;width:163px;height:3px;background:var(--red)}
.extras-list{left:516px;top:736px;list-style:none}
.extras-list li{display:flex;align-items:center;height:38px;font-weight:700;font-size:20px;letter-spacing:.3px}
.extras-list svg{width:24px;height:24px;margin-right:18px}
.skyline-art{left:0;top:966px;width:903px;height:86px}
.custodians{left:0;top:1052px;width:903px;height:66px;background:var(--band);border-top:3px solid var(--red);display:flex;align-items:center;justify-content:center;font-family:'Montserrat',sans-serif;font-weight:400;font-size:33px;letter-spacing:.5px}
.contact-band{left:0;top:1118px;width:903px;height:82px;background:linear-gradient(90deg,var(--red-deep),var(--red) 50%,var(--red-deep))}
.phone-pill{left:0;top:1129px;width:450px;height:52px;background:var(--white);border-radius:0 26px 26px 0;display:flex;align-items:center;padding-left:30px;color:var(--ink);font-weight:800;font-size:35px;white-space:nowrap}
.phone-pill svg{width:30px;height:30px;margin-right:14px}
.address{left:468px;top:1130px;width:270px;text-align:center;font-size:15px;font-weight:500;white-space:nowrap}
.address svg{display:block;margin:0 auto 6px;width:18px;height:20px}
.find-us{left:756px;top:1150px;display:flex;align-items:center;font-size:15px;white-space:nowrap}
.find-us i{display:inline-block;width:22px;height:22px;margin-left:10px;background:#e6e6e6;border-radius:3px}
</style>
</head>
<body>
<main class="flyer">
  <div class="abs hand-art" role="img" aria-label="Illustration of a hand holding a squeegee with cleaning tools hanging below" style="background:linear-gradient(180deg,#d8d8d8,#8a8a8a);opacity:.5;border-radius:0 0 12px 12px"></div>

  <div class="abs brand">
    <div class="brand-name">The Brightwells</div>
  </div>

  <div class="abs figure-art" role="img" aria-label="Red silhouette of a cleaner vacuuming" style="background:linear-gradient(180deg,#d2141c,#7a090e);opacity:.85;border-radius:60px 60px 16px 16px"></div>

  <div class="abs headline-script">Cleaning at its</div>
  <div class="abs headline-best">BEST</div>

  <p class="abs intro">The Brightwells We have been in business since 2008 and and are servicing multiple locations in san Jose CA . We provides custom tailored janitorial and facility maintenance programs to meet or exceed your expectations and budget.</p>

  <p class="abs services-lead">We provide services for</p>
  <ul class="abs service-list">
    <li><svg viewBox="0 0 24 22"><path d="M2 21V10h4v11zM8 21V6l4-4 4 4v15zM18 21V10h4v11z"/></svg>SCHOOLS</li>
    <li><svg viewBox="0 0 24 22"><path d="M3 10h14v2H3zM5 12h2v9H5zM13 12h2v9h-2zM18 6a2 2 0 110 4 2 2 0 010-4zM17 11h3v10h-3z"/></svg>OFFICES</li>
    <li><svg viewBox="0 0 24 22"><path d="M6 21V2h12v19zM8 4h2v2H8zM14 4h2v2h-2zM8 9h2v2H8zM14 9h2v2h-2zM8 14h2v2H8zM14 14h2v2h-2z"/></svg>OFFICE BUILDINGS</li>
    <li><svg viewBox="0 0 24 22"><path d="M2 8h3v6H2zM5 6h3v10H5zM8 10h8v2H8zM16 6h3v10h-3zM19 8h3v6h-3z"/></svg>GYMS</li>
    <li><svg viewBox="0 0 24 22"><path d="M12 0a2 2 0 110 4 2 2 0 010-4zM10 5h4l3 5-2 1-2-3v5l3 9h-2l-3-7-2 7H7l2-9V8l-3 3-1-1z"/></svg>DANCE STUDIOS</li>
  </ul>
  <div class="abs rule-short"></div>
  <div class="abs schedule">
    <svg viewBox="0 0 24 24" fill="none" stroke="#c0131b" stroke-width="2"><rect x="2" y="4" width="18" height="16" rx="2"/><path d="M2 9h18M7 2v4M15 2v4"/><circle cx="18" cy="18" r="4" fill="#121212"/></svg>
    <p>We provide janitorial services<strong>WEEKLY, BI-WEEKLY &amp; DAILY</strong></p>
  </div>

  <div class="abs rule-vertical"></div>
  <div class="abs extras-line"></div>
  <div class="abs extras-pill">WE ALSO PROVIDE</div>
  <ul class="abs extras-list">
    <li><svg viewBox="0 0 24 24" fill="none" stroke="#c0131b" stroke-width="2"><rect x="2" y="3" width="18" height="18" rx="3"/><path d="M7 12l4 4 10-12"/></svg>CARPET CLEANING</li>
    <li><svg viewBox="0 0 24 24" fill="none" stroke="#c0131b" stroke-width="2"><rect x="2" y="3" width="18" height="18" rx="3"/><path d="M7 12l4 4 10-12"/></svg>FLOORS STRIP AND WAX</li>
    <li><svg viewBox="0 0 24 24" fill="none" stroke="#c0131b" stroke-width="2"><rect x="2" y="3" width="18" height="18" rx="3"/><path d="M7 12l4 4 10-12"/></svg>FLOOR STEAMING</li>
    <li><svg viewBox="0 0 24 24" fill="none" stroke="#c0131b" stroke-width="2"><rect x="2" y="3" width="18" height="18" rx="3"/><path d="M7 12l4 4 10-12"/></svg>PERSONAL SUPERVISION</li>
    <li><svg viewBox="0 0 24 24" fill="none" stroke="#c0131b" stroke-width="2"><rect x="2" y="3" width="18" height="18" rx="3"/><path d="M7 12l4 4 10-12"/></svg>QUALITY CONTROL</li>
  </ul>

  <div class="abs skyline-art" role="img" aria-label="Red silhouette skyline of schools, offices, cleaners, a dancer and a gym" style="background:linear-gradient(180deg,rgba(192,19,27,0) 0%,rgba(192,19,27,.55) 55%,#b3121a 100%)"></div>

  <div class="abs custodians">WE HAVE UNIFORMED CUSTODIANS</div>

  <div class="abs contact-band"></div>
  <div class="abs phone-pill">
    <svg viewBox="0 0 30 30"><circle cx="15" cy="15" r="14" fill="#c0131b"/><path d="M11 8c1 0 2 3 2 4s-2 1-1 3 2 3 3 3 1-2 2-2 4 1 4 2-2 4-4 4c-4 0-9-6-9-10 0-2 2-4 3-4z" fill="#fff"/></svg>
    +1 555-014-2290
  </div>
  <div class="abs address">
    <svg viewBox="0 0 18 20"><path d="M9 0a7 7 0 017 7c0 5-7 13-7 13S2 12 2 7a7 7 0 017-7z" fill="#fff"/><circle cx="9" cy="7" r="3" fill="#c0131b"/></svg>
    PO Box 3307 Fernhill, Indiana
  </div>
  <div class="abs find-us">Find Us :<i></i></div>
</main>
</body>
</html>
```